Plume & Crest Hair Extensions needs a business card

We need a business card designed for an online luxury hair extensions business called Plume & Crest, we already have a logo and need an innovative business card (2-sided preferably). The strap line for the brand is 'Luxury Hair At Every Touchpoint!'. The brand is a premium brand selling virgin hair extensions and the target market is the mid-affluent ethnic woman as such the design should reflect this. The brand logo is grey and can be sent when requested.

Target Market(s)

25 to 35 year mid-affluent ethnic woman (Afro-American, Mixed Race, Asian)

Industry/Entity Type

Hair

Colors

Designer to choose colors to be used in the design.

Requirements
Must have
• Business Name: Plume and Crest
Strapline: Luxury hair at every touchpoint!
Domain: ​www.plumeandcrest.example
Email: info@plumeandcrest.example
sales and enquiries
44 07500 xxxxxxx

Please use the grey main brand logo depicted in page 2 of the attached pdf document

```html
<!DOCTYPE html>
<html lang="en">
<head>
<meta charset="utf-8">
<title>Plume &amp; Crest — Business Card</title>
<link rel="stylesheet" href="https://fonts.googleapis.com/css2?family=Josefin+Sans:wght@300&family=Questrial&display=swap">
<style>
  :root {
    --backdrop: #e7e7e9;
    --card-white: #ffffff;
    --brand-grey: #a7a8aa;
    --strap-grey: #9c9d9f;
    --logo-grey: #88898b;
    --text-on-grey: #ffffff;
    --illustration-grey: #b3b4b6;
  }
  * { box-sizing: border-box; margin: 0; padding: 0; }
  html, body {
    width: 1200px;
    height: 900px;
    overflow: hidden;
    background: var(--backdrop);
  }
  .card-set {
    position: absolute;
    inset: 0;
    display: flex;
    align-items: center;
    justify-content: center;
    gap: 60px;
  }
  .card {
    position: relative;
    width: 520px;
    height: 300px;
    border-radius: 22px;
    overflow: hidden;
    box-shadow: 0 10px 24px rgba(0, 0, 0, 0.10);
  }

  /* Front */
  .card--front { background: var(--card-white); }
  .front-band {
    position: absolute;
    left: 0; right: 0; bottom: 0;
    height: 48px;
    background: var(--brand-grey);
  }
  .front-illustration {
    position: absolute;
    left: 0;
    top: 18px;
    width: 180px;
    height: 190px;
    background: linear-gradient(160deg, rgba(179,180,182,0.35) 0%, var(--illustration-grey) 60%, rgba(179,180,182,0.6) 100%);
    border-radius: 0 60% 40% 0;
  }
  .strapline {
    position: absolute;
    top: 28px;
    right: 30px;
    text-align: right;
    font-family: "Josefin Sans", sans-serif;
    font-weight: 300;
    font-size: 31px;
    line-height: 1.12;
    letter-spacing: 0.5px;
    text-transform: uppercase;
    color: var(--strap-grey);
  }
  .brand-name {
    position: absolute;
    left: 28px;
    bottom: 64px;
    font-family: "Questrial", sans-serif;
    font-size: 27px;
    letter-spacing: 1.5px;
    color: var(--logo-grey);
  }

  /* Back */
  .card--back { background: var(--brand-grey); }
  .back-illustration {
    position: absolute;
    right: 0;
    top: 0;
    width: 200px;
    height: 100%;
    background: linear-gradient(200deg, rgba(255,255,255,0.85) 0%, rgba(255,255,255,0.45) 55%, rgba(255,255,255,0) 100%);
    border-radius: 70% 0 0 40%;
  }
  .web-address {
    position: absolute;
    left: 30px;
    top: 92px;
    font-family: "Questrial", sans-serif;
    font-size: 21px;
    color: var(--text-on-grey);
  }
  .contact {
    position: absolute;
    left: 30px;
    bottom: 44px;
    font-family: "Questrial", sans-serif;
    font-size: 16px;
    line-height: 1.3;
    color: var(--text-on-grey);
  }
  .contact-label { font-size: 17px; margin-bottom: 2px; }
</style>
</head>
<body>
  <main class="card-set">
    <section class="card card--front" aria-label="Business card front">
      <div class="front-illustration" role="img" aria-label="Grey illustration of a woman in profile with long flowing hair"></div>
      <p class="strapline">Luxury<br>Hair<br>At<br>Every<br>Touchpoint!</p>
      <p class="brand-name">Plume &amp; Crest</p>
      <div class="front-band"></div>
    </section>

    <section class="card card--back" aria-label="Business card back">
      <div class="back-illustration" role="img" aria-label="White illustration of flowing hair strands"></div>
      <p class="web-address">www.plumeandcrest.example</p>
      <div class="contact">
        <p class="contact-label">sales and enquiries</p>
        <p class="contact-phone">44 07500 xxxxxxx</p>
        <p class="contact-email">info@plumeandcrest.example</p>
      </div>
    </section>
  </main>
</body>
</html>
```